QMRB

Our company, Bright Harbour Wealth Coach, combines a Mortgage Broker Company and a Financial Planning Practice.
Our customers to get their finances in good shape by setting goals towards financial independence.
We design a path towards the goals and monitor progress in regular meetings.
Our customers achieve the goals by having a clear focus on what is important. Most importantly, we help eliminate waste by eliminating unnecessary taxes and unreasonably high interest rates on borrowings.
I have attached the logos for the two businesses combining. Maybe can include them as well. Not sure, could be too busy
Target Market(s)
People who are taking responsibility for their financial future aged 25 to 60 years old
Industry/Entity Type
Financial
Look and feel
Each slider illustrates characteristics of the customer's brand and the style your logo design should communicate.

```html
<!DOCTYPE html>
<html lang="en">
<head>
<meta charset="utf-8">
<title>Bright Harbour Wealth Coach – Banner</title>
<link rel="stylesheet" href="https://fonts.googleapis.com/css2?family=PT+Sans:wght@400;700&display=swap">
<style>
  :root {
    --stage: #3a3a3a;
    --brand-green: #5aa31a;
    --brand-blue: #1b80c8;
    --text-blue: #1a6fc0;
    --band-white: rgba(255, 255, 255, 0.86);
    --tile-light: #ffffff;
    --tile-dark: #000000;
  }
  * { box-sizing: border-box; margin: 0; padding: 0; }
  html, body {
    width: 1200px;
    height: 1000px;
    overflow: hidden;
    background: var(--stage);
    font-family: "PT Sans", "Tahoma", sans-serif;
  }
  .canvas { position: relative; width: 1200px; height: 1000px; }

  .banner {
    position: absolute;
    left: 174px;
    top: 342px;
    width: 851px;
    height: 315px;
    background: #fff;
    overflow: hidden;
  }
  .banner__top-bar {
    position: absolute; left: 0; top: 0; width: 100%; height: 7px;
    background: var(--brand-green);
  }
  .banner__photo {
    position: absolute; left: 0; top: 7px; width: 100%; height: 301px;
    background:
      linear-gradient(90deg,
        #c9766a 0%, #d9b64f 18%, #b85c7a 34%, #8fa56a 48%,
        #c7d3df 62%, #e6ecf2 80%, #dfe6ee 100%);
  }
  .banner__band {
    position: absolute; left: 0; top: 172px; width: 100%; height: 136px;
    background: var(--band-white);
  }
  .banner__bottom-bar {
    position: absolute; left: 0; bottom: 0; width: 100%; height: 7px;
    background: var(--brand-blue);
  }

  .brand-name {
    position: absolute;
    left: 54px;
    top: 207px;
    display: flex;
    align-items: center;
    gap: 12px;
  }
  .brand-name__dot {
    width: 22px; height: 22px; border-radius: 50%;
    background: var(--brand-blue);
  }
  .brand-name__text {
    color: var(--brand-blue);
    font-weight: 400;
    font-size: 25px;
    line-height: 28px;
  }

  .banner__divider {
    position: absolute; left: 336px; top: 207px;
    width: 3px; height: 73px;
    background: var(--brand-blue);
  }
  .banner__tagline {
    position: absolute; left: 352px; top: 205px;
    width: 480px;
    color: var(--text-blue);
    font-weight: 700;
    font-size: 19.5px;
    line-height: 22px;
  }

  .mark-tile {
    position: absolute;
    top: 684px;
    width: 180px;
    height: 180px;
    border-radius: 4px;
    display: flex;
    align-items: center;
    justify-content: center;
    text-align: center;
    color: var(--brand-blue);
    font-weight: 400;
    font-size: 22px;
    line-height: 26px;
  }
  .mark-tile--light { left: 172px; background: var(--tile-light); }
  .mark-tile--dark  { left: 369px; background: var(--tile-dark); }
</style>
</head>
<body>
<div class="canvas">
  <section class="banner">
    <div class="banner__top-bar"></div>
    <div class="banner__photo" role="img" aria-label="Photo of scattered Australian banknotes beside a printed spreadsheet of figures and a pen"></div>
    <div class="banner__band"></div>

    <div class="brand-name">
      <span class="brand-name__dot"></span>
      <span class="brand-name__text">Bright Harbour<br>Wealth Coach</span>
    </div>

    <div class="banner__divider"></div>
    <p class="banner__tagline">Our company, Bright Harbour Wealth Coach, combines a Mortgage Broker Company and a Financial Planning Practice</p>

    <div class="banner__bottom-bar"></div>
  </section>

  <div class="mark-tile mark-tile--light">Bright Harbour<br>Wealth Coach</div>
  <div class="mark-tile mark-tile--dark">Bright Harbour<br>Wealth Coach</div>
</div>
</body>
</html>
```